We are a General Practice - Family medicine
We also have Allied Health professionals working within our team

Industry/Entity Type

Business

Contact Information for Business Card

Front of the card to display:

ELMWOOD FAMILY CLINIC
PHONE 6381 2947

5/14 Kellerton Avenue
Ashbridge Northvale 7268

Back of the card to display:

My Appointments
Date:
Time:
With:

Please remember to phone us on 6381 2947 to cancel your appointment if you can't keep it.
A fee applied to missed appointments

```html
<!DOCTYPE html>
<html lang="en">
<head>
<meta charset="utf-8">
<title>Elmwood Family Clinic – Business Card</title>
<link rel="stylesheet" href="https://fonts.googleapis.com/css2?family=Open+Sans:wght@300;400;600&display=swap">
<style>
  :root {
    --bg: #ebebeb;
    --paper: #ffffff;
    --leaf-green: #9bcb3b;
    --sea-blue: #3aa8e0;
    --band: rgba(22, 48, 30, 0.74);
    --ink-dark: #1f3418;
    --ink-grey: #8a8f93;
    --ink-white: #ffffff;
  }
  html, body {
    margin: 0;
    width: 1200px;
    height: 944px;
    overflow: hidden;
    background: var(--bg);
    font-family: "Open Sans", Arial, sans-serif;
  }
  .canvas {
    position: relative;
    width: 1200px;
    height: 944px;
  }
  .card {
    position: absolute;
    top: 157px;
    width: 360px;
    height: 630px;
    background: var(--paper);
    overflow: hidden;
    box-shadow: 0 6px 18px rgba(0,0,0,0.18);
  }
  .card--front { left: 180px; }
  .card--back  { left: 660px; }

  .shape { position: absolute; border-radius: 50%; }
  .shape--blue  { width: 420px; height: 420px; left: -170px; top: 310px; background: var(--sea-blue); }
  .shape--green { width: 660px; height: 660px; left: 0; top: 310px; background: var(--leaf-green); }

  .brand {
    position: absolute;
    top: 132px;
    left: 0;
    right: 0;
    text-align: center;
  }
  .brand__name {
    display: inline-flex;
    align-items: center;
    gap: 10px;
    font-size: 24px;
    font-weight: 400;
    color: var(--ink-dark);
  }
  .brand__dot {
    width: 28px;
    height: 28px;
    background: var(--leaf-green);
  }
  .brand__tagline {
    margin-top: 6px;
    font-size: 10px;
    letter-spacing: 3px;
    color: var(--ink-grey);
    padding-left: 38px;
  }

  .band {
    position: absolute;
    left: 0;
    right: 0;
    background: var(--band);
    color: var(--ink-white);
  }
  .card--front .band {
    top: 420px;
    height: 64px;
    display: flex;
    align-items: center;
    justify-content: center;
    font-size: 20px;
    letter-spacing: 1px;
    white-space: nowrap;
  }
  .card--back .band {
    top: 500px;
    height: 62px;
    padding: 10px 24px;
    box-sizing: border-box;
    font-size: 9.5px;
    line-height: 1.45;
  }

  .contact {
    position: absolute;
    top: 510px;
    left: 90px;
    right: 20px;
    color: var(--ink-dark);
    font-size: 14px;
    line-height: 1.5;
  }
  .contact__row { display: flex; align-items: flex-start; gap: 12px; margin-bottom: 8px; }
  .contact__icon {
    flex: none;
    width: 22px;
    height: 22px;
    border-radius: 50%;
    background: var(--sea-blue);
    display: flex;
    align-items: center;
    justify-content: center;
    margin-top: 1px;
  }

  .appointments {
    position: absolute;
    top: 372px;
    left: 160px;
    color: var(--ink-dark);
    font-size: 15px;
    line-height: 1.75;
  }
  .appointments__title { font-weight: 600; }
</style>
</head>
<body>
<main class="canvas">

  <section class="card card--front" aria-label="Card front">
    <div class="shape shape--blue"></div>
    <div class="shape shape--green"></div>
    <div class="brand">
      <div class="brand__name"><span class="brand__dot"></span>Elmwood Family Clinic</div>
      <div class="brand__tagline">GENERAL PRACTICE</div>
    </div>
    <div class="band">ELMWOOD FAMILY CLINIC</div>
    <div class="contact">
      <div class="contact__row">
        <span class="contact__icon">
          <svg width="12" height="12" viewBox="0 0 24 24" aria-hidden="true"><path fill="#fff" d="M6.6 10.8a15 15 0 0 0 6.6 6.6l2.2-2.2a1 1 0 0 1 1-.25 11.4 11.4 0 0 0 3.6.57 1 1 0 0 1 1 1V20a1 1 0 0 1-1 1A17 17 0 0 1 3 4a1 1 0 0 1 1-1h3.5a1 1 0 0 1 1 1c0 1.25.2 2.45.57 3.57a1 1 0 0 1-.25 1z"/></svg>
        </span>
        <span>6381 2947</span>
      </div>
      <div class="contact__row">
        <span class="contact__icon">
          <svg width="12" height="12" viewBox="0 0 24 24" aria-hidden="true"><path fill="#fff" d="M12 2a7 7 0 0 0-7 7c0 5.2 7 13 7 13s7-7.8 7-13a7 7 0 0 0-7-7zm0 9.5A2.5 2.5 0 1 1 12 6.5a2.5 2.5 0 0 1 0 5z"/></svg>
        </span>
        <span>5/14 Kellerton Avenue<br>Ashbridge Northvale 7268</span>
      </div>
    </div>
  </section>

  <section class="card card--back" aria-label="Card back">
    <div class="shape shape--blue"></div>
    <div class="shape shape--green"></div>
    <div class="brand">
      <div class="brand__name"><span class="brand__dot"></span>Elmwood Family Clinic</div>
      <div class="brand__tagline">GENERAL PRACTICE</div>
    </div>
    <div class="appointments">
      <div class="appointments__title">My Appointments</div>
      <div>Date:</div>
      <div>Time:</div>
      <div>With:</div>
    </div>
    <div class="band">
      Please remember to phone us on 6381 2947 to cancel your appointment if you can't keep it.<br>
      A fee applied to missed appointments
    </div>
  </section>

</main>
</body>
</html>
```